looking for sleek business card to standout from the crowd!

We are a young biotechnology company looking to help you personalize your health through understanding your genetic make up. We need you help in making a clean but sleek business card design using our new logo. The goal? Any time we give our cards out, people say "nice card!" The feel we are going for is "modern-techy". We don't want to come across as an old, giant pharma company, but not trying to be a hipster either.

Target Market(s)

healthcare and biotechnology industry.

Industry/Entity Type

Biotechnology

Contact Information for Business Card

Info to include on the card will be NAME, TITLE, EMAIL, PHONE. The companies website (www.morvalytics.com) should also be on the card some where. Would like the logo, when printed, to be raised.

Requirements
Must have
• The logo we have attached in the color it is in. Fonts for text should lean toward more professional/tech.
Nice to have
• Prefer white/light color background
Should not have
• cartoons, landscape backgrounds images.

```html
<!DOCTYPE html>
<html lang="en">
<head>
<meta charset="utf-8">
<title>Morvalytics Business Card</title>
<link rel="stylesheet" href="https://fonts.googleapis.com/css2?family=Oswald:wght@500&family=Open+Sans:wght@400;600&display=swap">
<style>
  :root {
    --canvas-bg: #2b2b2d;
    --card-dark: #1e1e1f;
    --card-light: #ffffff;
    --logo-grey: #8c8c8e;
    --name-grey: #4a4a4c;
    --text-grey: #555557;
    --accent-green: #7cc242;
    --divider: #5a5a5c;
  }
  * { box-sizing: border-box; margin: 0; padding: 0; }
  html, body {
    width: 1200px;
    height: 1000px;
    overflow: hidden;
    background: var(--canvas-bg);
  }
  .canvas {
    position: relative;
    width: 1200px;
    height: 1000px;
  }
  .card {
    position: absolute;
    left: 250px;
    width: 700px;
    height: 400px;
    box-shadow: 0 10px 30px rgba(0,0,0,0.45);
  }
  .card--front {
    top: 60px;
    background: var(--card-dark);
    display: flex;
    align-items: center;
    justify-content: center;
  }
  .brand {
    display: flex;
    align-items: center;
    gap: 14px;
  }
  .brand__name {
    font-family: "Open Sans", sans-serif;
    font-weight: 600;
    font-size: 46px;
    letter-spacing: 3px;
    color: var(--logo-grey);
    text-transform: uppercase;
  }
  .brand__dot {
    width: 52px;
    height: 52px;
    border-radius: 50%;
    background: var(--logo-grey);
  }
  .card--back {
    top: 540px;
    background: var(--card-light);
  }
  .identity {
    position: absolute;
    left: 50px;
    top: 146px;
    width: 262px;
    text-align: right;
  }
  .identity__name {
    font-family: "Oswald", sans-serif;
    font-weight: 500;
    font-size: 42px;
    line-height: 1.05;
    color: var(--name-grey);
    letter-spacing: 1px;
    text-transform: uppercase;
  }
  .identity__title {
    font-family: "Open Sans", sans-serif;
    font-weight: 600;
    font-size: 18px;
    color: var(--accent-green);
    letter-spacing: 0.5px;
    margin-top: 2px;
  }
  .divider {
    position: absolute;
    left: 332px;
    top: 150px;
    width: 2px;
    height: 88px;
    background: var(--divider);
  }
  .contact {
    position: absolute;
    left: 356px;
    top: 144px;
    list-style: none;
    font-family: "Open Sans", sans-serif;
    font-size: 17px;
    line-height: 25px;
    color: var(--text-grey);
    white-space: nowrap;
  }
  .contact__accent { color: var(--accent-green); }
  .address {
    position: absolute;
    left: 0;
    right: 0;
    bottom: 56px;
    text-align: center;
    font-family: "Open Sans", sans-serif;
    font-size: 18px;
    color: var(--text-grey);
    letter-spacing: 0.5px;
  }
</style>
</head>
<body>
<main class="canvas">
  <section class="card card--front" aria-label="Card front">
    <div class="brand">
      <span class="brand__name">Morvalytics</span>
      <span class="brand__dot" aria-hidden="true"></span>
    </div>
  </section>

  <section class="card card--back" aria-label="Card back">
    <div class="identity">
      <h1 class="identity__name">Adrian Kole</h1>
      <p class="identity__title">CEO &amp; FOUNDER</p>
    </div>
    <div class="divider" aria-hidden="true"></div>
    <ul class="contact">
      <li>+000 318 562 047&nbsp; (Cell Phone)</li>
      <li>+000 274 903 615&nbsp; (Office)</li>
      <li>adrian@morvalytics.com</li>
      <li>www.<span class="contact__accent">morvalytics</span>.com</li>
    </ul>
    <p class="address">48 Harlow Lane, Brenmoor, 5821</p>
  </section>
</main>
</body>
</html>
```